Business Card Design

New business card design

Target Market(s)

Residential & Commercial Property Managers

Industry/Entity Type

Plumbing Services

Contact Information for Business Card

Name - Tom Brereton, title - Director, Phone Number - 0431 862 517, email - tom@rvk-plumbing.com.au, Company ABN - 73 512 938 204,

Font styles to use
Sans Serif

Colors
0054AA
0677BA
7BADD7
CADEEF
E8F1F8

```html
<!DOCTYPE html>
<html lang="en">
<head>
<meta charset="utf-8">
<title>RVK Plumbing Services – Business Card</title>
<link rel="stylesheet" href="https://fonts.googleapis.com/css2?family=Arimo:wght@400;700&display=swap">
<style>
  :root {
    --backdrop: #3d3d3d;
    --card-dark: #1f252b;
    --card-light: #ffffff;
    --brand-blue: #03adee;
    --ink-dark: #1f252b;
    --ink-light: #ffffff;
    --tagline-grey: #7a6f6a;
  }
  * { box-sizing: border-box; margin: 0; padding: 0; }
  html, body {
    width: 1200px;
    height: 803px;
    overflow: hidden;
    background: var(--backdrop);
    font-family: "Arimo", Arial, sans-serif;
  }
  .canvas { position: relative; width: 1200px; height: 803px; }

  .card {
    position: absolute;
    width: 525px;
    height: 300px;
    border-radius: 18px;
    overflow: hidden;
    box-shadow: 0 14px 30px rgba(0,0,0,0.35);
  }

  /* Front */
  .card--front { left: 55px; top: 120px; background: var(--card-dark); color: var(--ink-light); }
  .card__accent {
    position: absolute;
    right: 40px;
    top: 40px;
    width: 200px;
    height: 200px;
    border-radius: 50%;
    background: var(--brand-blue);
  }
  .brand-name {
    font-weight: 400;
    letter-spacing: 0.02em;
    white-space: nowrap;
  }
  .card--front .brand-name {
    position: absolute;
    left: 36px;
    top: 112px;
    font-size: 24px;
    color: var(--ink-light);
  }
  .contact { position: absolute; left: 36px; top: 168px; }
  .contact__name { font-weight: 700; font-size: 19px; color: var(--brand-blue); }
  .contact__title { font-size: 11px; margin-top: 2px; margin-bottom: 16px; }
  .contact__line {
    display: flex;
    align-items: center;
    gap: 8px;
    font-size: 12.5px;
    line-height: 19px;
  }
  .contact__icon { width: 11px; height: 11px; fill: var(--brand-blue); flex: none; }
  .contact__abn { padding-left: 19px; }

  /* Back */
  .card--back { left: 620px; top: 353px; background: var(--card-light); color: var(--ink-dark); }
  .card--back .brand-name {
    position: absolute;
    left: 0;
    right: 0;
    top: 128px;
    text-align: center;
    font-size: 34px;
    color: var(--ink-dark);
  }
</style>
</head>
<body>
<main class="canvas">
  <section class="card card--front" aria-label="Business card front">
    <div class="card__accent" aria-hidden="true"></div>
    <p class="brand-name">rvk plumbing services</p>
    <div class="contact">
      <p class="contact__name">Tom Brereton</p>
      <p class="contact__title">Director</p>
      <p class="contact__line">
        <svg class="contact__icon" viewBox="0 0 24 24" aria-hidden="true"><path d="M6.6 10.8a15.1 15.1 0 0 0 6.6 6.6l2.2-2.2c.3-.3.7-.4 1-.2 1.1.4 2.3.6 3.6.6.6 0 1 .4 1 1V20c0 .6-.4 1-1 1C10.6 21 3 13.4 3 4c0-.6.4-1 1-1h3.5c.6 0 1 .4 1 1 0 1.3.2 2.5.6 3.6.1.3 0 .7-.2 1z"/></svg>
        0431 862 517
      </p>
      <p class="contact__line">
        <svg class="contact__icon" viewBox="0 0 24 24" aria-hidden="true"><path d="M2 5h20v14H2zM4 7v.5l8 5 8-5V7l-8 5z"/></svg>
        tom@rvk-plumbing.com.au
      </p>
      <p class="contact__line contact__abn">ABN - 73 512 938 204</p>
    </div>
  </section>

  <section class="card card--back" aria-label="Business card back">
    <p class="brand-name">rvk plumbing services</p>
  </section>
</main>
</body>
</html>
```